PREMIUM AGENCY High End Business Card - A+++ Designers Wanted

** DO NOT ATTEMPT TO CONTACT ME THROUGH SEARCHING ON ZINTREL OR EMAILING ME THROUGH MY WEBSITE **

I need a fresh, contemporary business card designed using the logo attached (BRONSALK)

I have attached the font for BRONSALK

It must have a premium look and feel. The business card size must be STANDARD size.

You can submit either/both VERTICAL or HORIZONTAL designs.

FRONT: It must have the following sample information on

Paul Ardley
Director Operations
Mobile +61 452 118 906
Email paulardley@bronsalk.com
www.bronsalk.com

The REAR of the business card must have the words

IMAGINE SHAPE BEYOND

as part of the design, in the same font (NEXA) attached.

The words do not need to be in capitals, or on the same line, please design this as you see it best working.

ADDITIONAL INFORMATION
======================

The BRONSALK logo must be on the front of the card

I want Ultraviolet printing on the final design, to enhance either the NAME of the person OR the BRONSALK logo OR the words on the back of the card.

Target Market(s)

Agency, Advertising Agency, Creative, Designers

Industry/Entity Type

Media

Contact Information for Business Card

Design Agency, Contemporary, Premium look and feel, High Quality

Font styles to use
Serif
Sans Serif
Other font styles liked:
• ATTACHED TO PROJECT

Requirements
Must have
• BLACK & WHITE as the primary design, and if you feel there can be a highlighted colour, then this can be used.
• The Logo ICON attached is blue, this colour must not be changed.
• I have attached the partner brand BRONSALK MEDIA incase you need to manipulate the original files.
• ** DO NOT ATTEMPT TO CONTACT ME THROUGH SEARCHING ON ZINTREL OR EMAILING ME THROUGH MY WEBSITE **
Nice to have
• Must be Premium. I have attached some sample designs, that I like that would be a good inspiration for where this can be taken.
• My favourite design is is the KESTRAVUE2-BUSINESSCARD-TEMPLATE
Should not have
• No funny or silly standard / off the shelf designs

```html
<!DOCTYPE html>
<html lang="en">
<head>
<meta charset="utf-8">
<title>Bronsalk Media – Business Card</title>
<link href="https://fonts.googleapis.com/css2?family=Montserrat:wght@300;400;500;700&display=swap" rel="stylesheet">
<style>
  :root {
    --bg: #2b2b2d;
    --card: #050505;
    --blue: #22a9e1;
    --white: #ffffff;
    --muted: #d8d8d8;
    --ghost: #0c2230;
  }
  html, body {
    margin: 0;
    padding: 0;
    width: 1200px;
    height: 900px;
    overflow: hidden;
    background: var(--bg);
    font-family: "Montserrat", sans-serif;
  }
  .canvas { position: relative; width: 1200px; height: 900px; }
  .card {
    position: absolute;
    width: 600px;
    height: 343px;
    border-radius: 22px;
    overflow: hidden;
    background: var(--card);
    box-shadow: 0 14px 30px rgba(0,0,0,0.45);
  }
  .card--back { left: 70px; top: 70px; }
  .card--front { left: 530px; top: 480px; }
  .card svg { display: block; width: 600px; height: 343px; }
  .brand-bold { font-weight: 700; fill: var(--white); }
  .brand-light { font-weight: 300; fill: var(--white); }
  .back-mark { font-weight: 700; fill: var(--blue); letter-spacing: 3px; }
  .ghost-mark { font-weight: 700; fill: var(--ghost); letter-spacing: 4px; }
  .tagline { font-weight: 500; fill: var(--white); letter-spacing: 0.5px; }
  .name { font-weight: 500; fill: var(--blue); }
  .role { font-weight: 300; fill: var(--white); }
  .contact { font-weight: 400; fill: var(--muted); }
  .contact-accent { fill: var(--blue); }
  .rule { stroke: var(--white); stroke-width: 1.2; }
  .icon { fill: none; stroke: var(--blue); stroke-width: 1.6; }
  .icon-solid { fill: var(--blue); }
</style>
</head>
<body>
<main class="canvas">

  <section class="card card--back" aria-label="Card back">
    <svg viewBox="0 0 600 343">
      <text class="back-mark" x="300" y="185" font-size="48" text-anchor="middle">BRONSALK</text>
    </svg>
  </section>

  <section class="card card--front" aria-label="Card front">
    <svg viewBox="0 0 600 343">
      <text class="ghost-mark" x="300" y="62" font-size="42" text-anchor="middle">BRONSALK</text>

      <g class="logo">
        <circle cx="40" cy="112" r="8" class="icon-solid"/>
        <text x="58" y="121" font-size="25"><tspan class="brand-bold">BRONSALK</tspan><tspan class="brand-light" dx="4">MEDIA</tspan></text>
      </g>

      <g class="identity">
        <text class="name" x="580" y="120" font-size="20" text-anchor="end">PAUL ARDLEY</text>
        <line class="rule" x1="420" y1="130" x2="600" y2="130"/>
        <text class="role" x="580" y="148" font-size="12.5" text-anchor="end">Director Operations</text>
      </g>

      <g class="tag">
        <text class="tagline" x="40" y="200" font-size="17">IMAGINE SHAPE BEYOND</text>
        <line class="rule" x1="0" y1="212" x2="330" y2="212"/>
      </g>

      <g class="contacts">
        <path class="icon" d="M44 232c1 4 4 8 8 9l2-2-2-2-2 1c-1-1-3-3-3-4l1-2-2-2z"/>
        <text class="contact" x="66" y="242" font-size="14">+61 452 118 906</text>

        <rect class="icon" x="43" y="253" width="13" height="9" rx="1"/>
        <path class="icon" d="M43 254l6.5 5 6.5-5"/>
        <text class="contact" x="66" y="263" font-size="14">paulardley@bronsalk.com</text>

        <circle class="icon" cx="49.5" cy="279" r="6"/>
        <path class="icon" d="M43.5 279h12M49.5 273c-3 4-3 8 0 12M49.5 273c3 4 3 8 0 12"/>
        <text class="contact" x="66" y="284" font-size="14">www.<tspan class="contact-accent">bronsalk</tspan>.com</text>
      </g>

      <polygon points="0,322 360,304 380,343 0,343" fill="var(--white)"/>
      <polygon points="0,330 365,312 372,343 0,343" fill="var(--card)"/>
      <polygon points="392,268 600,218 600,343 380,343 368,300" fill="var(--blue)"/>
      <polygon points="368,300 380,343 372,343 360,304" fill="var(--white)"/>
    </svg>
  </section>

</main>
</body>
</html>
```